LOLU Baby Massage Classes - flyer to make a difference

I need a single page flyer, preferably single page, to hand out to doctors, medical centres and parents. To also leave on counters of establishments.
It is to promote my baby massage classes. Mums can get together with other mums and book a 5 week course to learn and discover the many benefits of baby massage.
Benefits include: enhances bonding and attachment, understand non-verbal cues from your baby, helps with sleep patterns, help with immune system, increases vagal activity,relief from wind, colic or constipation to name some.

Baby age from birth to 12 months. Group classes or private sessions

I am a Professional Member and Certified by the Global Society of Newborn Touch (GSNT) GSNT Australia is Nationally Accredited and is endorsed by Crown Academy of Carers, the Southern Guild of Birth Attendants, The Southern Union of Daily Living Therapy Australia, The Southern Union of Bodywork Practitioner and is a full member of Wellmind Network Australia.

Class detail and availability contact is Petra Holm 0487 315 208 petra.joanne.holm@quillmail.example www.lolunewborntouch com.au facebook/comLOLUnewborntouch

My colour scheme is green and purple as you will see from my logo and website. I would like my flyer to be softer tones of either both colours or just one.

I will include some images you can choose from or show me any you think will fit in with baby massage. THANK YOU
Updates

Hi The size of my flyer is A6. Approx 150mms x 210mms and single sided. Thank you

Target Market(s)

mums and dads, groups, doctors, midwives

Industry/Entity Type

Medical

Font styles to use
Sans Serif

Colors
87d0c7
b09cc8

Requirements
Must have
• baby photo or photos, both my logo and the GSNT logo. The GSNT logo is to be small
• Baby Massage Classes (wording) is very important to catch the eye.
• Invitation to book a class or gather friends to book is next in importance
• Benefits is next
• The admin information ie.,membership, certification and endorsements are lesser and can be small.
• Contact information to be noticeable.
Nice to have
• If you have an idea, drawing or photo that would look better, please feel free to try it
Should not have
• should not be crowded with information all the same size

```html
<!DOCTYPE html>
<html lang="en">
<head>
<meta charset="utf-8">
<title>LOLU Baby Massage Classes flyer</title>
<link rel="stylesheet" href="https://fonts.googleapis.com/css2?family=Chewy&family=Acme&family=Open+Sans:ital,wght@0,400;0,600;0,700;1,400&display=swap">
<style>
  :root {
    --page: #ffffff;
    --mint: #3fdf9c;
    --deep-green: #1f7a4a;
    --lime: #86f01e;
    --lime-soft: #a6f45a;
    --purple: #7d2fd8;
    --peach: #fde0a9;
    --white: #ffffff;
    --ink: #1d1d1d;
    --brown: #4a2a10;
    --teal-logo: #49d59a;
  }
  * { margin: 0; padding: 0; box-sizing: border-box; }
  html, body { width: 1000px; height: 1200px; overflow: hidden; background: var(--page); }
  .canvas { position: relative; width: 1000px; height: 1200px; overflow: hidden; background: var(--page); font-family: "Open Sans", sans-serif; }
  .flyer { position: absolute; left: 95px; top: 42px; width: 800px; height: 1128px; background: var(--mint); box-shadow: 0 2px 8px rgba(0,0,0,.25); }
  .shapes { position: absolute; left: 0; top: 0; width: 1000px; height: 1200px; z-index: 1; }
  .brand { position: absolute; z-index: 2; left: 160px; top: 180px; display: flex; align-items: center; gap: 10px; }
  .brand-dot { width: 52px; height: 52px; border-radius: 50%; background: var(--teal-logo); }
  .brand-name { font-family: "Acme", sans-serif; font-size: 34px; color: var(--teal-logo); letter-spacing: 1px; }
  .title { position: absolute; z-index: 3; font-family: "Chewy", "Acme", sans-serif; line-height: 1; white-space: nowrap; paint-order: stroke fill; }
  .title-baby { left: 198px; top: 398px; font-size: 62px; color: var(--purple); -webkit-text-stroke: 6px var(--white); }
  .title-massage { left: 108px; top: 440px; font-size: 108px; color: var(--lime); -webkit-text-stroke: 9px var(--white); text-shadow: 0 3px 0 rgba(0,0,0,.15); }
  .title-classes { left: 302px; top: 532px; font-size: 38px; color: var(--purple); -webkit-text-stroke: 6px var(--white); }
  .invite { position: absolute; z-index: 2; left: 128px; top: 572px; color: var(--white); font-family: "Acme", sans-serif; }
  .invite-main { font-size: 29px; line-height: 1.1; }
  .invite-sub { font-size: 17px; }
  .benefits-box { position: absolute; z-index: 2; left: 115px; top: 635px; width: 405px; height: 355px; background: var(--lime); border: 4px solid var(--white); outline: 3px solid var(--deep-green); border-radius: 22px; overflow: hidden; }
  .benefits-title { font-family: "Acme", sans-serif; font-weight: 400; color: var(--white); font-size: 36px; line-height: 40px; margin: 50px 0 10px 17px; }
  .benefits-list { list-style: none; padding: 0 16px 0 18px; color: var(--white); font-size: 17px; line-height: 22.5px; }
  .benefits-list li { position: relative; padding-left: 18px; }
  .benefits-list li::before { content: "\2714"; position: absolute; left: 0; font-size: 12px; }
  .details-strip { list-style: none; position: absolute; left: 0; right: 0; bottom: 0; height: 60px; background: var(--lime-soft); padding: 8px 0 0 22px; }
  .details-strip li { color: var(--brown); font-style: italic; font-size: 15px; line-height: 21px; }
  .course { position: absolute; z-index: 2; left: 530px; top: 626px; width: 350px; text-align: center; color: var(--white); font-weight: 700; font-size: 19px; line-height: 26px; }
  .course-number { font-family: "Chewy", "Acme", sans-serif; color: var(--purple); font-size: 56px; line-height: 54px; margin-top: 8px; -webkit-text-stroke: 6px var(--white); paint-order: stroke fill; }
  .course-length { font-family: "Chewy", "Acme", sans-serif; color: var(--purple); font-size: 27px; line-height: 28px; -webkit-text-stroke: 6px var(--white); paint-order: stroke fill; margin-bottom: 14px; }
  .credentials { position: absolute; z-index: 2; left: 615px; top: 880px; width: 250px; text-align: center; color: var(--ink); }
  .credentials-name { font-family: "Acme", sans-serif; font-size: 21px; line-height: 24px; margin-bottom: 2px; }
  .credentials-text { font-size: 13.5px; line-height: 19px; }
  .credentials-badge { width: 28px; height: 28px; border-radius: 50%; background: var(--purple); margin: 10px auto 0; opacity: .7; }
  .contact { position: absolute; z-index: 2; left: 118px; top: 1018px; color: var(--white); }
  .contact-heading { font-family: "Acme", sans-serif; font-size: 20px; margin-bottom: 10px; }
  .contact-line { font-size: 17px; line-height: 19px; }
  .contact-name { font-style: italic; }
</style>
</head>
<body>
<div class="canvas">
  <div class="flyer"></div>

  <svg class="shapes" viewBox="0 0 1000 1200" xmlns="http://www.w3.org/2000/svg">
    <defs>
      <linearGradient id="photoTones" x1="0" y1="0" x2="1" y2="1">
        <stop offset="0" stop-color="#e9b98e"/>
        <stop offset=".5" stop-color="#d8a784"/>
        <stop offset="1" stop-color="#6a8fb8"/>
      </linearGradient>
      <linearGradient id="portraitTones" x1="0" y1="0" x2="0" y2="1">
        <stop offset="0" stop-color="#d9cfc0"/>
        <stop offset=".55" stop-color="#e7b8a0"/>
        <stop offset="1" stop-color="#6b38c7"/>
      </linearGradient>
    </defs>
    <path class="hero-outline" d="M375 320 C385 440 450 535 545 552 C650 568 800 545 895 500" fill="none" stroke="#1f7a4a" stroke-width="26"/>
    <path class="hero-photo" role="img" aria-label="Photo of mums in a class leaning over their babies on mats, baby in front looking up" d="M375 42 H895 V500 C800 545 650 565 545 552 C450 535 385 440 375 320 Z" fill="url(#photoTones)" stroke="#ffffff" stroke-width="12"/>
    <path class="logo-panel" d="M135 42 H375 V245 A120 118 0 0 1 135 245 Z" fill="#ffffff" stroke="#1f7a4a" stroke-width="8"/>
    <circle class="toy-decoration" role="img" aria-label="Small baby rattle illustration" cx="352" cy="375" r="20" fill="#f4a623"/>
    <path class="blob" d="M112 575 C150 555 300 560 440 570 C455 600 440 640 420 650 C330 662 200 660 112 655 C100 630 100 595 112 575 Z" fill="#8a2fd0"/>
    <rect class="bottle-decoration" role="img" aria-label="Baby bottle illustration" x="350" y="600" width="110" height="42" rx="16" transform="rotate(28 405 621)" fill="#3fb889"/>
    <circle class="credentials-circle" cx="742" cy="1012" r="150" fill="#fde0a9" stroke="#1f7a4a" stroke-width="6"/>
    <rect class="portrait" role="img" aria-label="Portrait photo of the instructor in a purple top" x="435" y="892" width="172" height="278" rx="60" fill="url(#portraitTones)" stroke="#ffffff" stroke-width="6"/>
  </svg>

  <div class="brand"><span class="brand-dot"></span><span class="brand-name">lolu</span></div>

  <div class="title title-baby">Baby</div>
  <div class="title title-massage">Massage</div>
  <div class="title title-classes">Classes</div>

  <div class="invite">
    <div class="invite-main">Book a class</div>
    <div class="invite-sub">or gather friends to book</div>
  </div>

  <section class="benefits-box">
    <h2 class="benefits-title">Benefits include:</h2>
    <ul class="benefits-list">
      <li>enhances bonding and attachment</li>
      <li>understand non-verbal cues from your baby</li>
      <li>helps with sleep patterns</li>
      <li>help with immune system</li>
      <li>increases vagal activity</li>
      <li>relief from wind, colic or constipation to name some.</li>
    </ul>
    <ul class="details-strip">
      <li>&#8226; Baby age from birth to 12 months.</li>
      <li>&#8226; Group classes or private sessions</li>
    </ul>
  </section>

  <div class="course">
    <p>Mums can get together with<br>other mums and book a</p>
    <div class="course-number">5</div>
    <div class="course-length">week course</div>
    <p>to learn and discover the many<br>benefits of baby massage.</p>
  </div>

  <div class="credentials">
    <div class="credentials-name">Petra Holm</div>
    <p class="credentials-text">Certified by the Global<br>Society of Newborn Touch<br>(GSNT), Australia<br>Nationally Accredited and is<br>endorsed by Crown Academy<br>of Carers, the Southern Guild<br>of Birth Attendants, The<br>Southern Union of Daily<br>Living Therapy Australia.</p>
    <div class="credentials-badge"></div>
  </div>

  <div class="contact">
    <div class="contact-heading">For Class detail and availability contact</div>
    <div class="contact-line contact-name">Petra Holm</div>
    <div class="contact-line">0487 315 208</div>
    <div class="contact-line">petra.joanne.holm@quillmail.example</div>
    <div class="contact-line">www.lolunewborntouch com.au</div>
    <div class="contact-line">facebook/comLOLUnewborntouch</div>
  </div>
</div>
</body>
</html>
```